Vosk and Telby Website

Vosk & Telby Website

The purpose of the Vosk & Telby website has 2 purposes; number 1 is to SALE the most “Rugged and Reliable products with the most versatile innovation possible. Number 2 to attract and assist territory sales manager across the United States with an easy flow website and customer sales support in the background.

Our Website Vision

This Website should be very modern and professional with a easy flow, we will use the following platform and plug-ins built with then website builder Divi Word press with Woo commerce with a sales professional CRM ( submit the plug-in of your choice for review before adding to programming) in the backend. We will provide information to the look we are looking for. All background images will be Black and White. We will provide professional images of our products that have been trimmed out and saved with a transparent background so that they can be added to a custom designed background or black and white image that will enhance the product. I want all the special tools provided in the Divi Family of tools used to give this website the WOW FACTOR. As of Now or site will be hosted on Plume Vault

Header design should have a Center VT Logo provided with a Hamburger Menu on the left and on the right a Search Glass Icon a Person Icon for login and register and Sales Cart Icon this could in the only Page that is Full Page Black and White image that can be blurred or ghosted back as we want the main page to be a line of 6 to 8 different Carts and Dollies to represent our products in color. Designer can take the images of our product and color correct Photoshop or whatever is needed to make it look its best. That is the landing or main image. The home page will be a slider of up to five images with 4 major messages to our customer or reasons to do business with Vosk & Telby. I will download 2 image to give you a idea of direction.

Slider Messages: Price Match Guarantee
Industry Best Warranty 5 Years on Frame 3 Years on Casters
Customize to fit your Surface and Application
Designed, Engineered and Manufactured Proudly in the U.S.A.

Categories/ Products Page
Carts
Dollies
Casters
Used Equipment

Categories Page

Products Page
Ratings with stars and comments
WooCommerce Composite products

Customization Page

Career Page

Contact page

Policy Page

Terms and Conditions Page

LOOK AT ZELMIRAB7BAY.COM WEBSITE MUST BE BETTER

Target Market(s)

We are a manufacturer of the worlds most rugged and reliable Industrial carts, dollies, hand trucks and casters. we will be selling to all types of industry's from distributors warehouse hospitals

Industry/Entity Type

Light Industrial

Coding

Coded - Design and coding required

Number of Pages Required

5+ page

Colors
ec1f27

Requirements
Must have
• Monochrome with Products colored and buttons and logo color codes in logo are Red # AF002A and Gray #5B5C5E
• Divi we own a lifetime license
• WordPress
• Woocommerce
• woocommerce composite products
• WP forms
• CRM
• Welder image is meant to be used Customization Page
Nice to have
• CRM for our 100 plus reps

```html
<!DOCTYPE html>
<html lang="en">
<head>
<meta charset="utf-8">
<title>Casters – Vosk &amp; Telby</title>
<link href="https://fonts.googleapis.com/css2?family=IBM+Plex+Sans:wght@400;600&family=Rubik:wght@500;700&display=swap" rel="stylesheet">
<style>
  :root {
    --brand-red: #af002a;
    --button-red: #ec1f27;
    --brand-gray: #5b5c5e;
    --ink: #333333;
    --body-text: #4a4a4a;
    --page-bg: #f6f4f4;
    --white: #ffffff;
    --social: #3b3d40;
  }
  * { box-sizing: border-box; margin: 0; padding: 0; }
  html, body { width: 1200px; height: 1112px; overflow: hidden; }
  body { font-family: "IBM Plex Sans", sans-serif; background: var(--white); color: var(--ink); position: relative; }

  .site-header { height: 90px; background: var(--white); position: relative; }
  .menu-toggle { position: absolute; left: 132px; top: 34px; width: 29px; height: 24px; display: flex; flex-direction: column; justify-content: space-between; }
  .menu-toggle span { display: block; height: 5px; background: var(--brand-gray); border-radius: 1px; }
  .brand { position: absolute; left: 50%; top: 26px; transform: translateX(-50%); display: flex; align-items: center; gap: 10px; }
  .brand-mark { width: 38px; height: 38px; background: var(--brand-red); border-radius: 4px; }
  .brand-name { font-family: "Rubik", sans-serif; font-weight: 700; font-size: 32px; line-height: 38px; color: var(--brand-gray); letter-spacing: 1px; white-space: nowrap; }
  .header-tools { position: absolute; right: 132px; top: 34px; display: flex; gap: 22px; align-items: center; }

  .catalog { position: absolute; top: 90px; left: 0; width: 1200px; height: 944px; background: var(--page-bg); }
  .catalog-title { font-family: "Rubik", sans-serif; font-weight: 700; font-size: 26px; line-height: 32px; color: var(--brand-gray); text-align: center; position: absolute; top: 36px; width: 100%; letter-spacing: 0.5px; }
  .product-grid { position: absolute; left: 132px; top: 105px; display: grid; grid-template-columns: repeat(4, 220px); column-gap: 18.6px; row-gap: 21px; }
  .product-card { height: 379px; background: var(--white); text-align: center; position: relative; box-shadow: 0 1px 2px rgba(0,0,0,0.04); }
  .product-card > * { position: absolute; left: 0; right: 0; }
  .product-image { width: 120px; height: 112px; left: 50px; right: auto; top: 37px; background: linear-gradient(160deg, #9c9c9c, #5e5e5e); border-radius: 4px; }
  .product-name { top: 190px; font-weight: 600; font-size: 16px; line-height: 24px; letter-spacing: 0.4px; color: var(--ink); }
  .product-desc { top: 223px; font-size: 12.8px; line-height: 17.6px; color: var(--body-text); padding: 0 8px; }
  .product-price { top: 272px; font-family: "Rubik", sans-serif; font-weight: 500; font-size: 19px; line-height: 26px; color: var(--brand-red); }
  .add-to-cart { top: 317px; left: 55.5px; right: auto; width: 109px; height: 28px; line-height: 28px; background: var(--button-red); color: var(--white); font-family: "Rubik", sans-serif; font-weight: 700; font-size: 12px; letter-spacing: 0.3px; }

  .site-footer { position: absolute; top: 1034px; left: 0; width: 1200px; height: 78px; background: var(--white); }
  .follow { position: absolute; left: 131px; top: 26px; display: flex; align-items: center; gap: 7px; font-size: 14px; color: var(--ink); }
  .follow-label { margin-right: 3px; }
  .social-dot { width: 27px; height: 27px; border-radius: 50%; background: var(--social); }
  .copyright { position: absolute; right: 130px; top: 31px; font-size: 14px; line-height: 18px; color: var(--ink); }
</style>
</head>
<body>
  <header class="site-header">
    <div class="menu-toggle" aria-label="Menu"><span></span><span></span><span></span></div>
    <div class="brand">
      <div class="brand-mark"></div>
      <div class="brand-name">VOSK &amp; TELBY</div>
    </div>
    <div class="header-tools">
      <svg width="26" height="26" viewBox="0 0 26 26" aria-label="Search"><circle cx="11" cy="11" r="8" fill="none" stroke="#5b5c5e" stroke-width="3.5"/><line x1="17" y1="17" x2="24" y2="24" stroke="#5b5c5e" stroke-width="4" stroke-linecap="round"/></svg>
      <svg width="30" height="26" viewBox="0 0 30 26" aria-label="Cart"><path d="M1 3h5l4 14h15l3-10H8" fill="none" stroke="#5b5c5e" stroke-width="3" stroke-linejoin="round"/><path d="M8 7h20l-3 10H10z" fill="#5b5c5e"/><circle cx="12" cy="22.5" r="2.5" fill="#5b5c5e"/><circle cx="23" cy="22.5" r="2.5" fill="#5b5c5e"/></svg>
    </div>
  </header>

  <main class="catalog">
    <h1 class="catalog-title">CASTERS</h1>
    <div class="product-grid">
      <article class="product-card"><div class="product-image" role="img" aria-label="Product photo: lift hand truck"></div><h2 class="product-name">LOREM IPSUM</h2><p class="product-desc">Lorem Ipsum is simply dummy<br>text of the printing ad .</p><div class="product-price">$1939.99</div><a class="add-to-cart">ADD TO CART</a></article>
      <article class="product-card"><div class="product-image" role="img" aria-label="Product photo: steel box cart"></div><h2 class="product-name">LOREM IPSUM</h2><p class="product-desc">Lorem Ipsum is simply dummy<br>text of the printing ad .</p><div class="product-price">$1939.99</div><a class="add-to-cart">ADD TO CART</a></article>
      <article class="product-card"><div class="product-image" role="img" aria-label="Product photo: mesh basket cart"></div><h2 class="product-name">LOREM IPSUM</h2><p class="product-desc">Lorem Ipsum is simply dummy<br>text of the printing ad .</p><div class="product-price">$1939.99</div><a class="add-to-cart">ADD TO CART</a></article>
      <article class="product-card"><div class="product-image" role="img" aria-label="Product photo: pallet stacker"></div><h2 class="product-name">LOREM IPSUM</h2><p class="product-desc">Lorem Ipsum is simply dummy<br>text of the printing ad .</p><div class="product-price">$1939.99</div><a class="add-to-cart">ADD TO CART</a></article>
      <article class="product-card"><div class="product-image" role="img" aria-label="Product photo: platform lift truck"></div><h2 class="product-name">LOREM IPSUM</h2><p class="product-desc">Lorem Ipsum is simply dummy<br>text of the printing ad .</p><div class="product-price">$1939.99</div><a class="add-to-cart">ADD TO CART</a></article>
      <article class="product-card"><div class="product-image" role="img" aria-label="Product photo: mobile lift table"></div><h2 class="product-name">LOREM IPSUM</h2><p class="product-desc">Lorem Ipsum is simply dummy<br>text of the printing ad .</p><div class="product-price">$1939.99</div><a class="add-to-cart">ADD TO CART</a></article>
      <article class="product-card"><div class="product-image" role="img" aria-label="Product photo: two-shelf utility cart"></div><h2 class="product-name">LOREM IPSUM</h2><p class="product-desc">Lorem Ipsum is simply dummy<br>text of the printing ad .</p><div class="product-price">$1939.99</div><a class="add-to-cart">ADD TO CART</a></article>
      <article class="product-card"><div class="product-image" role="img" aria-label="Product photo: poly bulk truck"></div><h2 class="product-name">LOREM IPSUM</h2><p class="product-desc">Lorem Ipsum is simply dummy<br>text of the printing ad .</p><div class="product-price">$1939.99</div><a class="add-to-cart">ADD TO CART</a></article>
    </div>
  </main>

  <footer class="site-footer">
    <div class="follow">
      <span class="follow-label">Follow us</span>
      <span class="social-dot" aria-label="Social profile"></span>
      <span class="social-dot" aria-label="Social profile"></span>
      <span class="social-dot" aria-label="Social profile"></span>
    </div>
    <div class="copyright">Copyright © 2019 All Rights Reserved</div>
  </footer>
</body>
</html>
```